Podcast Cover Art for Fast Growing Show (Ill include a gracious tip!)

This artwork is for "The Steadfast Fellow Show." The podcast is for men, and it's all about self-improvement, confidence, success, money, women and masculinity. It's for the guy who wants to improve himself. I'd like for my picture to be included — in black and white — and I want the text to read: "The Steadfast Fellow Show" and somewhere in there it'll say: "with Dale Prowen." I'm open to color schemes. The podcast is a little edgy so I'd like for that to be represented in the design. Thank you! (((Here's the podcast page if you wanna check it out: http://steadfastfellowshow.castorbit.net/)))

Target Market(s)

Men who want to attract women and improve their lives!

Font styles to use
Serif

Colors

Designer to choose colors to be used in the design.

Requirements
Must have
• My image in it (in black and white) and the two titles: "The Steadfast Fellow Show" and "with Dale Prowen"
Nice to have
• My logo in it somehow (which is the arrow looking logo attached below). I've also found that my image looks best in black and white and with a circular type cut out (although I'm open to different design ideas). I've attached my logo with a circular cut out below so you can see what I'm talking about.
Should not have
• Flowers. Teddy bears. ice cream.

```html
<!DOCTYPE html>
<html lang="en">
<head>
<meta charset="UTF-8">
<title>The Steadfast Fellow Show – Cover Art</title>
<link rel="stylesheet" href="https://fonts.googleapis.com/css2?family=League+Spartan:wght@800&family=Roboto+Condensed:wght@700&display=swap">
<style>
  :root {
    --ink: #0b0b0b;
    --crimson: #9c0404;
    --paper: #ffffff;
    --vignette-light: #ffffff;
    --vignette-mid: #dcdcdc;
    --vignette-dark: #868686;
    --photo-light: #b4b4b4;
    --photo-mid: #8a8a8a;
    --photo-dark: #333333;
  }
  * { margin: 0; padding: 0; box-sizing: border-box; }
  html, body {
    width: 1200px;
    height: 1000px;
    overflow: hidden;
    background: var(--paper);
  }
  .cover {
    position: absolute;
    left: 140px;
    top: 40px;
    width: 920px;
    height: 920px;
    overflow: hidden;
    background: radial-gradient(ellipse 70% 70% at 50% 55%, var(--vignette-light) 0%, var(--vignette-light) 35%, var(--vignette-mid) 70%, var(--vignette-dark) 100%);
  }
  .title-line {
    position: absolute;
    font-family: "League Spartan", sans-serif;
    font-weight: 800;
    line-height: 1;
    white-space: nowrap;
    letter-spacing: -2px;
  }
  .title-the { left: 51px; top: 54px; font-size: 116px; color: var(--ink); }
  .title-steadfast { left: 48px; top: 151px; font-size: 116px; color: var(--crimson); }
  .title-fellow { left: 48px; top: 268px; font-size: 114px; color: var(--crimson); }
  .title-fellow .show-word { color: var(--ink); margin-left: 22px; }
  .accent-rule {
    position: absolute;
    left: 298px;
    top: 75px;
    width: 622px;
    height: 12px;
    background: var(--crimson);
  }
  .host-photo {
    position: absolute;
    left: 0;
    top: 0;
    width: 920px;
    height: 920px;
  }
  .brand-mark {
    position: absolute;
    left: 58px;
    top: 436px;
    display: flex;
    align-items: center;
    gap: 8px;
    font-family: "League Spartan", sans-serif;
    font-weight: 800;
    font-size: 40px;
    line-height: 1;
    color: var(--ink);
  }
  .brand-mark .brand-square {
    width: 16px;
    height: 16px;
    background: var(--ink);
  }
  .host-credit {
    position: absolute;
    left: 599px;
    top: 394px;
    font-family: "Roboto Condensed", sans-serif;
    font-weight: 700;
    white-space: nowrap;
  }
  .host-credit .with {
    display: block;
    margin-left: 6px;
    font-size: 54px;
    line-height: 1;
    color: var(--ink);
  }
  .host-credit .host-name {
    display: inline-block;
    margin-top: 6px;
    padding: 6px 12px 4px;
    background: var(--crimson);
    color: var(--paper);
    font-size: 48px;
    line-height: 1.1;
    letter-spacing: -0.5px;
    white-space: nowrap;
  }
</style>
</head>
<body>
  <main class="cover">
    <div class="accent-rule"></div>
    <div class="title-line title-the">THE</div>
    <div class="title-line title-steadfast">STEADFAST</div>
    <div class="title-line title-fellow">FELLOW<span class="show-word">SHOW</span></div>

    <svg class="host-photo" viewBox="0 0 920 920" role="img" aria-label="Black and white portrait of host Dale Prowen, hands pressed together at his chin, wearing a dark ribbed zip sweater">
      <defs>
        <linearGradient id="photo-tone" x1="0" y1="0" x2="0" y2="1">
          <stop offset="0" stop-color="var(--photo-light)"/>
          <stop offset="0.45" stop-color="var(--photo-mid)"/>
          <stop offset="1" stop-color="var(--photo-dark)"/>
        </linearGradient>
      </defs>
      <path fill="url(#photo-tone)" d="M45 920 L120 700 Q140 650 230 635 L330 610 L322 470 Q310 328 450 328 Q590 328 580 470 L575 610 L680 630 Q800 650 830 720 L884 920 Z"/>
    </svg>

    <div class="brand-mark"><span class="brand-square"></span>SFS</div>

    <div class="host-credit">
      <span class="with">with</span>
      <span class="host-name">DALE PROWEN</span>
    </div>
  </main>
</body>
</html>
```